Billboard design 8x3M NURA (Spanish company)

We´re located in the south of Spain. We run a local telecom company.
We sell Fiber optic, and mobile phone lines mainly.
The billboard will have to be in Spanish, I would like the price to be something you spot on first sight when passing by in the car.
Our company color is blue, like in our logo which I will add. I will also add a example from what we currently have.
The new offer should be:
1000 megas + 100Gigas movil con llamadas ilimitadas. (meaning 1000Mb fiber optic speed and 100Gb data and unlimited calls for 1 mobile line)
Our details are: phone line 952 00 0147
Website: nu-ra.es

```html
<!DOCTYPE html>
<html lang="es">
<head>
<meta charset="utf-8">
<title>NURA – Valla 8x3</title>
<link rel="stylesheet" href="https://fonts.googleapis.com/css2?family=Montserrat:wght@700;800;900&display=swap">
<style>
  :root {
    --page-bg: #e8edf6;
    --navy: #0f2f9e;
    --blue: #1a46c8;
    --blue-bright: #2f7cf0;
    --cyan: #5cc8ff;
    --rule: rgba(170, 200, 255, 0.55);
    --white: #ffffff;
    --yellow: #ffe11a;
  }
  * { margin: 0; padding: 0; box-sizing: border-box; }
  html, body {
    width: 1200px;
    height: 800px;
    overflow: hidden;
    background: var(--page-bg);
    font-family: "Montserrat", sans-serif;
  }
  .billboard {
    position: absolute;
    left: 30px;
    top: 150px;
    width: 1140px;
    height: 501px;
    background: var(--blue);
    overflow: hidden;
  }
  .top-bar {
    position: absolute;
    left: 0; top: 0;
    width: 100%;
    height: 89px;
    background: linear-gradient(90deg, var(--navy), var(--blue) 50%, var(--navy));
    border-bottom: 2px solid var(--rule);
  }
  .brand-name {
    position: absolute;
    left: 60px;
    top: 18px;
    font-size: 50px;
    font-weight: 800;
    color: var(--white);
    letter-spacing: -1px;
  }
  .tagline {
    position: absolute;
    left: 370px;
    right: 40px;
    top: 28px;
    text-align: center;
    font-size: 31px;
    font-weight: 700;
    color: var(--white);
    letter-spacing: -0.3px;
  }
  .offer-area {
    position: absolute;
    left: 0; top: 89px;
    width: 100%;
    height: 336px;
    background:
      radial-gradient(ellipse at 50% 55%, rgba(92, 200, 255, 0.45), transparent 60%),
      linear-gradient(180deg, #1540c0, #1f5ae0 50%, #1440bf);
  }
  .art-cable {
    position: absolute;
    left: 70px; top: 106px;
    width: 240px; height: 128px;
    border-radius: 20px;
    background: linear-gradient(110deg, #1d58d8, var(--cyan));
    opacity: 0.85;
  }
  .art-phone {
    position: absolute;
    left: 880px; top: 46px;
    width: 200px; height: 246px;
    border-radius: 24px;
    background: linear-gradient(160deg, #4c8cf2, #1236b0);
    transform: skewX(-8deg);
  }
  .price {
    position: absolute;
    left: 0; right: 0;
    top: 4px;
    text-align: center;
    padding-left: 16px;
    font-size: 134px;
    font-weight: 900;
    line-height: 1;
    color: var(--yellow);
    letter-spacing: -5px;
    text-shadow: 0 4px 10px rgba(10, 30, 110, 0.5);
  }
  .offer-line {
    position: absolute;
    left: 0; right: 0;
    text-align: center;
    font-weight: 800;
    line-height: 1;
    color: var(--white);
    text-shadow: 0 2px 6px rgba(10, 30, 110, 0.5);
  }
  .offer-line.main { top: 178px; font-size: 39px; padding-left: 70px; }
  .offer-line.main .plus { color: var(--yellow); }
  .offer-line.main .unit { font-size: 29px; }
  .offer-line.calls { top: 229px; font-size: 33px; padding-left: 58px; }
  .bottom-bar {
    position: absolute;
    left: 0; top: 425px;
    width: 100%;
    height: 76px;
    background: linear-gradient(90deg, var(--navy), var(--blue) 50%, var(--navy));
    border-top: 2px solid var(--rule);
  }
  .contact-phone {
    position: absolute;
    left: 150px; top: 14px;
    display: flex;
    align-items: center;
    gap: 10px;
    font-size: 42px;
    font-weight: 700;
    color: var(--white);
  }
  .contact-phone svg { width: 40px; height: 40px; }
  .contact-web {
    position: absolute;
    right: 146px; top: 14px;
    font-size: 42px;
    font-weight: 700;
    color: var(--white);
  }
</style>
</head>
<body>
  <div class="billboard">
    <header class="top-bar">
      <div class="brand-name">NU-RA</div>
      <div class="tagline">INTERNET ULTRARRÁPIDO EN TU ZONA</div>
    </header>

    <section class="offer-area">
      <div class="art-cable" role="img" aria-label="Ilustración de un conector de cable de red con estelas de luz"></div>
      <div class="art-phone" role="img" aria-label="Ilustración de un teléfono móvil 5G con destellos de luz"></div>
      <div class="price">29,90€</div>
      <div class="offer-line main">1000 MEGAS <span class="plus">+</span> 100<span class="unit">GB</span> MÓVIL</div>
      <div class="offer-line calls">LLAMADAS ILIMITADAS</div>
    </section>

    <footer class="bottom-bar">
      <div class="contact-phone">
        <svg viewBox="0 0 24 24" aria-hidden="true">
          <path fill="#ffffff" d="M6.6 10.8a15.1 15.1 0 0 0 6.6 6.6l2.2-2.2a1 1 0 0 1 1-.25 11.4 11.4 0 0 0 3.6.57 1 1 0 0 1 1 1V20a1 1 0 0 1-1 1A17 17 0 0 1 3 4a1 1 0 0 1 1-1h3.5a1 1 0 0 1 1 1c0 1.250.2 2.45.57 3.6a1 1 0 0 1-.25 1z"/>
        </svg>
        <span>952 00 0147</span>
      </div>
      <div class="contact-web">nu-ra.es</div>
    </footer>
  </div>
</body>
</html>
```